Online interactive calendar for training organisation

We have a new website being made and need a design for an online calendar that is interactive and very simple and easy to use. On our main page this calendar will include all of our courses (approx 30 different ones with up to 8 different locations). On our sub pages which have course information, the calendar will only include details of that specific course. Details needed are: Course code, course name/title, date, duration (1/2 day - 5 days), location, price, discount price. Maybe also a key for available or limited spots left? We want a section at the top of the calendar to be able to filter by location or course, and maybe to filter by month also? I have included a spreadsheet with a sample of our courses with this information. Also a sample draft of the main page on our new webpage to show the colour green which is our company colour. Main notes - we want as simple, effective and easy to use as possible.
We will need to know what plug in we can use to get the design you have created.

Target Market(s)

Mining and construction - both companies and individuals

Number of Pages Required

1 page

Colors
cadf82

Requirements
Must have
• Be simple, easy to use, effective.

```html
<!DOCTYPE html>
<html lang="en">
<head>
<meta charset="utf-8">
<title>Sitewise Safety – Time Table</title>
<link href="https://fonts.googleapis.com/css2?family=Roboto+Condensed:wght@400;700&family=Roboto:wght@400;500;700&display=swap" rel="stylesheet">
<style>
:root{
  --green:#93c83c;
  --green-bright:#3cc63c;
  --red:#ee2a2a;
  --ink:#2b2b2b;
  --text:#444;
  --muted:#666;
  --line:#dcdcdc;
  --hero:#d6d6d6;
  --footer:#2b2b2b;
  --white:#fff;
}
*{box-sizing:border-box;margin:0;padding:0}
html,body{width:1200px;height:3169px;overflow:hidden}
body{position:relative;font-family:"Roboto",Arial,sans-serif;color:var(--text);background:var(--white)}
.abs{position:absolute}
.topbar{left:0;top:0;width:1200px;height:44px;background:var(--green)}
.social{display:flex;gap:12px}
.social span{width:22px;height:22px;border-radius:50%;background:var(--white);display:block}
.topbar .social{position:absolute;left:151px;top:11px}
.search{left:424px;top:8px;width:352px;height:29px;background:var(--white);border-radius:2px;font-size:12px;color:#555;padding:8px 22px}
.search svg{position:absolute;right:22px;top:6px}
.student{left:936px;top:6px;width:113px;height:33px;background:var(--ink);color:var(--white);font-size:12px;font-weight:500;border-radius:2px;display:flex;align-items:center;justify-content:center}
.header{left:0;top:44px;width:1200px;height:62px;background:var(--white)}
.brand{position:absolute;left:150px;top:12px;display:flex;align-items:center;gap:8px}
.brand-dot{width:34px;height:34px;border-radius:50%;background:var(--red)}
.brand-name{font-family:"Roboto",sans-serif;font-weight:700;font-size:17px;color:var(--red);line-height:1}
.brand-sub{font-size:7.5px;color:var(--ink);letter-spacing:.5px;margin-top:3px;font-weight:500}
.nav{position:absolute;right:152px;top:24px;display:flex;gap:22px;font-size:12px;color:var(--ink)}
.nav .active{color:var(--green)}
.hero{left:0;top:106px;width:1200px;height:703px;background:radial-gradient(ellipse at 50% 40%,#dedede,#cfcfcf)}
.hero h1{position:absolute;top:82px;width:100%;text-align:center;font-family:"Roboto Condensed",sans-serif;font-weight:700;font-size:44px;color:var(--ink)}
.hero p{position:absolute;top:142px;width:100%;text-align:center;font-family:"Roboto Condensed",sans-serif;font-size:19px;color:var(--ink)}
.hero .rule{position:absolute;left:556px;top:176px;width:88px;height:3px;background:var(--green)}
.tile{width:168px}
.tile .ph{height:162px}
.tile .cap{text-align:center;font-size:13px;color:var(--ink);margin-top:13px}
.ph{width:100%}
.tt-title{left:0;top:892px;width:1200px;text-align:center;font-family:"Roboto Condensed",sans-serif;font-weight:700;font-size:29px;color:var(--ink)}
.filter-label{left:289px;top:988px;font-size:13px;font-weight:500;color:var(--ink)}
.select{width:168px;height:37px;border:1px solid #bbb;border-radius:2px;font-size:12px;color:#555;padding:12px 15px;background:var(--white)}
.select svg{position:absolute;right:14px;top:15px}
.course{left:150px;width:915px;height:195px;border-bottom:1px solid var(--line)}
.course .ph{position:absolute;left:0;top:0;width:150px;height:150px}
.course .info{position:absolute;left:183px;top:22px;width:700px}
.course h3{font-weight:500;font-size:19px;color:var(--ink)}
.course h3 small{font-weight:400;font-size:12.5px}
.meta{position:absolute;font-size:11.5px;color:#555;display:flex;align-items:center;gap:7px}
.price{position:absolute;font-family:"Roboto Condensed",sans-serif;font-size:17px;font-weight:700;display:flex;gap:20px}
.price s{font-weight:400;color:#666}
.price .now{color:var(--green)}
.price .only{color:var(--ink)}
.badge{position:absolute;height:21px;width:113px;color:var(--white);font-size:8px;font-weight:700;display:flex;align-items:center;justify-content:center;border-radius:2px}
.badge.limited{background:var(--red)}
.badge.open{background:var(--green-bright);width:94px}
.pager{left:488px;top:2269px;display:flex;align-items:center;font-size:11px;color:#666}
.pager .btn{width:30px;height:38px;display:flex;align-items:center;justify-content:center}
.pager .prev{background:var(--green)}
.pager .next{border:2px solid var(--green)}
.pager .num{width:28px;text-align:center}
.pager .cur{font-weight:700;color:var(--ink)}
.banner{left:0;top:2395px;width:1200px;height:449px;background:linear-gradient(100deg,#8a9298 0%,#b9c0c4 35%,#c9b54a 50%,#d4c060 58%,#b8b6a8 72%,#eeeeee 85%)}
.banner-box{left:793px;top:2463px;width:255px;height:313px;background:rgba(255,255,255,.85);box-shadow:0 4px 8px rgba(0,0,0,.25)}
.banner-box .inner{position:absolute;left:19px;top:19px;width:217px;height:275px;background:linear-gradient(180deg,#e3e8ec,#d6dad6)}
.banner-title{left:705px;top:2547px;width:360px;font-family:"Roboto Condensed",sans-serif;font-weight:700;font-size:38px;line-height:47px;color:var(--ink)}
.banner-strip{left:705px;top:2653px;width:343px;height:32px;background:var(--green);color:var(--white);font-size:11.5px;display:flex;align-items:center;justify-content:center}
.footer{left:0;top:2844px;width:1200px;height:264px;background:var(--footer)}
.footer .brand{left:150px;top:70px}
.footer .brand-dot{width:28px;height:28px}
.footer .social{position:absolute;left:178px;top:128px}
.footer .nav{top:64px;color:var(--white)}
.fcontact{top:119px;font-size:12px;color:var(--white);display:flex;align-items:center;gap:7px}
.copy{left:0;top:3108px;width:1200px;height:61px;background:var(--green);color:var(--white);font-size:10px;display:flex;align-items:center;justify-content:center}
</style>
</head>
<body>
<svg width="0" height="0" style="position:absolute">
  <defs>
    <symbol id="i-cal" viewBox="0 0 12 12"><rect x="0.5" y="1.5" width="11" height="10" fill="none" stroke="#93c83c"/><rect x="0.5" y="1.5" width="11" height="3" fill="#93c83c"/><rect x="2.5" y="6" width="2" height="2" fill="#93c83c"/><rect x="5" y="6" width="2" height="2" fill="#93c83c"/><rect x="7.5" y="6" width="2" height="2" fill="#93c83c"/></symbol>
    <symbol id="i-clock" viewBox="0 0 12 12"><circle cx="6" cy="6" r="5.5" fill="#93c83c"/><path d="M6 3v3.3l2 1.2" stroke="#fff" stroke-width="1.2" fill="none"/></symbol>
    <symbol id="i-pin" viewBox="0 0 10 14"><path d="M5 0a5 5 0 0 1 5 5c0 3.5-5 9-5 9S0 8.5 0 5a5 5 0 0 1 5-5z" fill="#93c83c"/><circle cx="5" cy="5" r="2" fill="#fff"/></symbol>
    <symbol id="i-mail" viewBox="0 0 14 10"><rect width="14" height="10" fill="#93c83c"/><path d="M0 0l7 5 7-5" stroke="#2b2b2b" fill="none"/></symbol>
    <symbol id="i-down" viewBox="0 0 10 6"><path d="M1 1l4 4 4-4" stroke="#333" stroke-width="1.5" fill="none"/></symbol>
  </defs>
</svg>

<div class="abs topbar">
  <div class="social"><span></span><span></span><span></span><span></span></div>
</div>
<div class="abs search">Search
  <svg width="18" height="18" viewBox="0 0 18 18"><circle cx="7" cy="7" r="5.5" stroke="#333" stroke-width="2" fill="none"/><path d="M11 11l5.5 5.5" stroke="#333" stroke-width="2"/></svg>
</div>
<div class="abs student">Student Access</div>

<header class="abs header">
  <div class="brand"><span class="brand-dot"></span><div><div class="brand-name">SITEWISE SAFETY</div><div class="brand-sub">SAFETY AND TRAINING</div></div></div>
  <nav class="nav"><span class="active">Home</span><span>Courses</span><span>Our Services</span><span>About us</span><span>Funding</span><span>Locations</span><span>Contact us</span></nav>
</header>

<section class="abs hero">
  <h1>The Sitewise Safety Difference</h1>
  <p>Committed to helping our students succeed.</p>
  <div class="rule"></div>
</section>

<div class="abs tile" style="left:150px;top:316px"><div class="ph" role="img" aria-label="Open-cut mine with haul trucks" style="background:linear-gradient(#6d6258,#4a443c)"></div><div class="cap">All Courses</div></div>
<div class="abs tile" style="left:337px;top:316px"><div class="ph" role="img" aria-label="Worker cutting timber with circular saw" style="background:linear-gradient(#d8d4cc,#9a8e80)"></div><div class="cap">Funded Courses</div></div>
<div class="abs tile" style="left:524px;top:316px"><div class="ph" role="img" aria-label="Mining excavator on dusty site" style="background:linear-gradient(#b7bcc1,#8b7c6b)"></div><div class="cap">Mining</div></div>
<div class="abs tile" style="left:711px;top:316px"><div class="ph" role="img" aria-label="Excavator moving rocks" style="background:linear-gradient(#5e5e5e,#3c3c3c)"></div><div class="cap">Standard 11</div></div>
<div class="abs tile" style="left:898px;top:316px"><div class="ph" role="img" aria-label="Workers on a timber roof frame" style="background:linear-gradient(#c6d2de,#8c5a4a)"></div><div class="cap">Work safely at heights</div></div>
<div class="abs tile" style="left:150px;top:525px"><div class="ph" role="img" aria-label="Team meeting with sticky notes on a board" style="background:linear-gradient(#e8e6e2,#b6aca0)"></div><div class="cap">Corporate Clients</div></div>
<div class="abs tile" style="left:337px;top:525px"><div class="ph" role="img" aria-label="Hands typing on a laptop" style="background:linear-gradient(#4c4440,#2e2a28)"></div><div class="cap">Online Courses</div></div>
<div class="abs tile" style="left:524px;top:525px"><div class="ph" role="img" aria-label="Person signing a document at a desk" style="background:linear-gradient(#5a4a3e,#2e2620)"></div><div class="cap">RPL'S &amp; VOC'S</div></div>
<div class="abs tile" style="left:711px;top:525px"><div class="ph" role="img" aria-label="Workers laying steel reinforcement" style="background:linear-gradient(#8a949a,#5e6a70)"></div><div class="cap">Plant &amp; Equipment</div></div>
<div class="abs tile" style="left:898px;top:525px"><div class="ph" role="img" aria-label="Construction crew on a building slab" style="background:linear-gradient(#b4b0aa,#7a6a60)"></div><div class="cap">Construction</div></div>

<h2 class="abs tt-title">Time Table</h2>
<div class="abs filter-label">Filter by</div>
<div class="abs select" style="left:360px;top:980px">Location<svg width="10" height="6"><use href="#i-down"/></svg></div>
<div class="abs select" style="left:551px;top:980px">Course<svg width="10" height="6"><use href="#i-down"/></svg></div>
<div class="abs select" style="left:741px;top:980px">Month<svg width="10" height="6"><use href="#i-down"/></svg></div>

<article class="abs course" style="top:1084px">
  <div class="ph" role="img" aria-label="Workers climbing scaffolding" style="background:linear-gradient(#a9b6c0,#7a5a40)"></div>
  <div class="info"><h3>Work Safely at Heights <small>(Course ID :- RIIHAN304D)</small></h3></div>
  <div class="meta" style="left:183px;top:57px"><svg width="12" height="12"><use href="#i-cal"/></svg>10/29/2019</div>
  <div class="meta" style="left:383px;top:56px"><svg width="10" height="14"><use href="#i-pin"/></svg>Yatala</div>
  <div class="meta" style="left:183px;top:83px"><svg width="12" height="12"><use href="#i-clock"/></svg>8 am ( Duration 1 day )</div>
  <div class="badge limited" style="left:383px;top:82px">LIMITED SPOTS LEFT</div>
  <div class="price" style="left:183px;top:107px"><s>$ 500</s><span class="now">$ 120</span></div>
</article>

<article class="abs course" style="top:1279px">
  <div class="ph" role="img" aria-label="Forklift inside a container" style="background:linear-gradient(#3a3a3a,#7a746a)"></div>
  <div class="info"><h3>Forklift <small>(Course ID :- RIIMPO308E)</small></h3></div>
  <div class="meta" style="left:183px;top:57px"><svg width="12" height="12"><use href="#i-cal"/></svg>10/30/2019</div>
  <div class="meta" style="left:383px;top:56px"><svg width="10" height="14"><use href="#i-pin"/></svg>Mackay</div>
  <div class="meta" style="left:183px;top:83px"><svg width="12" height="12"><use href="#i-clock"/></svg>8 am ( Duration 3 day )</div>
  <div class="badge limited" style="left:383px;top:82px">LIMITED SPOTS LEFT</div>
  <div class="price" style="left:183px;top:107px"><s>$ 500</s><span class="now">$ 100</span></div>
</article>

<article class="abs course" style="top:1474px">
  <div class="ph" role="img" aria-label="Scaffolding around a building" style="background:linear-gradient(#bcd0dc,#5a6e78)"></div>
  <div class="info"><h3>Basic Scaffolding <small>(Course ID :- TLIL0005)</small></h3></div>
  <div class="meta" style="left:183px;top:57px"><svg width="12" height="12"><use href="#i-cal"/></svg>11/4/2019</div>
  <div class="meta" style="left:383px;top:56px"><svg width="10" height="14"><use href="#i-pin"/></svg>Townsville</div>
  <div class="meta" style="left:183px;top:83px"><svg width="12" height="12"><use href="#i-clock"/></svg>8 am ( Duration 5 day )</div>
  <div class="badge limited" style="left:383px;top:82px">LIMITED SPOTS LEFT</div>
  <div class="price" style="left:183px;top:107px"><s>$ 500</s><span class="now">$ 200</span></div>
</article>

<article class="abs course" style="top:1669px">
  <div class="ph" role="img" aria-label="Orange first aid case" style="background:linear-gradient(#f0603a,#c8401e)"></div>
  <div class="info"><h3>First Aid - practical only <small>(Course ID :- HLTAID001)</small></h3></div>
  <div class="meta" style="left:183px;top:57px"><svg width="12" height="12"><use href="#i-cal"/></svg>11/15/2019</div>
  <div class="meta" style="left:383px;top:56px"><svg width="10" height="14"><use href="#i-pin"/></svg>Moranbah</div>
  <div class="meta" style="left:183px;top:83px"><svg width="12" height="12"><use href="#i-clock"/></svg>1 pm ( Duration 1/2 day )</div>
  <div class="badge open" style="left:383px;top:82px">AVAILABLE</div>
  <div class="price" style="left:183px;top:107px"><span class="only">$ 80</span></div>
</article>

<article class="abs course" style="top:1864px">
  <div class="ph" role="img" aria-label="Gloved hand taking a test sample" style="background:linear-gradient(#3e3a36,#c49a84)"></div>
  <div class="info"><h3>Drug and Alcohol testing</h3></div>
  <div class="meta" style="left:183px;top:57px"><svg width="12" height="12"><use href="#i-cal"/></svg>By appointment</div>
  <div class="meta" style="left:383px;top:56px"><svg width="10" height="14"><use href="#i-pin"/></svg>Moranbah</div>
  <div class="meta" style="left:183px;top:83px"><svg width="12" height="12"><use href="#i-clock"/></svg>Duration 30 mins</div>
  <div class="price" style="left:183px;top:107px"><span class="only">$ 88</span></div>
</article>

<article class="abs course" style="top:2059px">
  <div class="ph" role="img" aria-label="Supervisors in an office meeting" style="background:linear-gradient(#e4e6e8,#7a808a)"></div>
  <div class="info"><h3>Supervisors <small>(Course ID :- S123)</small></h3></div>
  <div class="meta" style="left:183px;top:57px"><svg width="12" height="12"><use href="#i-cal"/></svg>12/10/2019</div>
  <div class="meta" style="left:383px;top:56px"><svg width="10" height="14"><use href="#i-pin"/></svg>Moranbah</div>
  <div class="meta" style="left:183px;top:83px"><svg width="12" height="12"><use href="#i-clock"/></svg>7 am ( Duration 1 day )</div>
  <div class="badge open" style="left:383px;top:82px">AVAILABLE</div>
  <div class="price" style="left:183px;top:107px"><s>$ 450</s><span class="now">$ 100</span></div>
</article>

<nav class="abs pager">
  <span class="btn prev"><svg width="7" height="10"><path d="M6 1L2 5l4 4" stroke="#fff" stroke-width="1.5" fill="none"/></svg></span>
  <span class="num" style="margin-left:12px">&nbsp;</span>
  <span class="num cur">1</span><span class="num">2</span><span class="num">3</span><span class="num">4</span><span class="num">5</span>
  <span class="num">&nbsp;</span>
  <span class="btn next"><svg width="7" height="10"><path d="M1 1l4 4-4 4" stroke="#93c83c" stroke-width="1.5" fill="none"/></svg></span>
</nav>

<section class="abs banner" role="img" aria-label="Yellow mining haul truck on a dirt road under cloudy sky"></section>
<div class="abs banner-box"><div class="inner"></div></div>
<h2 class="abs banner-title">Training a Safety<br>Culture that Counts</h2>
<div class="abs banner-strip">Now Traning - Working at Heights &amp; Confined Spaces Courses</div>

<footer class="abs footer">
  <div class="brand"><span class="brand-dot"></span><div class="brand-name">SITEWISE SAFETY</div></div>
  <div class="social"><span></span><span></span><span></span><span></span></div>
  <nav class="nav"><span>Home</span><span>Courses</span><span>Our Services</span><span>About us</span><span>Funding</span><span>Locations</span><span>Contact us</span></nav>
  <div class="abs fcontact" style="left:590px"><svg width="10" height="14"><use href="#i-pin"/></svg>18 Harbour Road, Yatala QLD 4207</div>
  <div class="abs fcontact" style="left:891px"><svg width="14" height="10"><use href="#i-mail"/></svg>info@sitewisesafety.example</div>
</footer>
<div class="abs copy">Copyright © 2019 All Rights Reserved | Powered by Sitewise Safety.</div>
</body>
</html>
```